Brivelle LLC Website Redesign Productct (HTML/CSS NEEDED)

We are looking for a new website to replace our current site www.brivellecare.example. We would like to be able to offer richer content with more pictures as well as create a design that integrates with our new logo (attached).

Target Market(s)

Our target market consists of home care agencies, and human services not for profits.

Font styles to use
Sans Serif

Requirements
Must have
• Design integrated with new logo

```html
<!DOCTYPE html>
<html lang="en">
<head>
<meta charset="utf-8">
<title>Brivelle — Web-based Healthcare Management System</title>
<link href="https://fonts.googleapis.com/css2?family=Bebas+Neue&family=Lato:wght@400;700&family=Open+Sans:ital,wght@0,400;0,600;0,700;1,400;1,700&display=swap" rel="stylesheet">
<style>
:root{
  --purple:#7d6cc6;
  --purple-dark:#6a59b5;
  --purple-text:#7467bd;
  --teal:#3fcccb;
  --cyan:#1fbde6;
  --cyan-deep:#0fa9d6;
  --ink:#444;
  --grey-bg:#f3f3f3;
  --footer:#222;
  --footer-bar:#333;
  --white:#fff;
}
*{margin:0;padding:0;box-sizing:border-box}
html,body{width:801px;height:1200px;overflow:hidden;background:var(--white)}
body{position:relative;font-family:"Open Sans",Arial,sans-serif;color:var(--ink)}
.abs{position:absolute}

/* header */
.site-header{position:absolute;left:0;top:0;width:801px;height:63px;background:linear-gradient(#fff,#ececec)}
.header-band{position:absolute;left:0;top:0}
.brand{position:absolute;left:92px;top:14px;display:flex;align-items:center;gap:7px}
.brand-dot{width:28px;height:28px;border-radius:50%;background:var(--cyan)}
.brand-name{font:700 27px/1 "Open Sans",sans-serif;color:#555}
.brand-tag{position:absolute;left:138px;top:44px;font:400 5px/1 "Open Sans",sans-serif;color:#777;letter-spacing:.2px}
.top-actions{position:absolute;top:7px;right:87px;display:flex;gap:6px}
.top-btn{height:19px;padding:0 6px;background:var(--teal);border-radius:3px;color:#fff;font:700 9px/19px "Open Sans",sans-serif;display:flex;align-items:center;gap:4px}
.top-btn svg{width:10px;height:10px}
.main-nav{position:absolute;top:37px;left:327px;display:flex;font:400 11px/1 "Lato",sans-serif;color:#fff}
.main-nav span{padding:0 13px;border-left:1px dotted rgba(255,255,255,.5)}
.main-nav span:first-child{padding-left:0;border:0}

/* hero */
.hero{position:absolute;left:0;top:63px;width:801px;height:314px;background:radial-gradient(ellipse at 35% 45%,#bdbdbd 0%,#8e8e8e 35%,#4a4a4a 60%,#cfcfcf 85%)}
.hero-card{position:absolute;left:430px;top:157px;width:284px;height:143px;background:var(--cyan);text-align:right;padding:18px 28px 0 0;color:#fff}
.hero-card .h-cond{font:400 22px/1 "Bebas Neue",sans-serif;letter-spacing:.5px}
.hero-card .h-sans{font:700 17px/1.1 "Open Sans",sans-serif;margin:7px 0 5px}
.hero-card .h-cond.lg{font-size:24px}
.hero-more{position:absolute;right:27px;top:108px;width:73px;height:17px;border-radius:9px;background:#fff;color:#222;font:700 8px/17px "Open Sans",sans-serif;text-align:left;padding-left:7px}
.hero-more i{position:absolute;right:3px;top:3px;width:11px;height:11px;border-radius:50%;background:var(--cyan-deep)}

/* welcome */
.welcome-title{position:absolute;top:388px;left:0;width:801px;display:flex;justify-content:center;align-items:center;gap:10px;font:300 19px/1 "Open Sans",sans-serif;color:#555}
.welcome-title .mark{display:flex;align-items:center;gap:6px;font-weight:700;color:#555;font-size:19px}
.welcome-title .mark b{width:18px;height:18px;border-radius:50%;background:var(--cyan)}
.rule{position:absolute;height:1px;background:linear-gradient(90deg,transparent,#ddd,transparent)}
.lead{position:absolute;top:443px;left:88px;width:625px;text-align:center;font:400 11px/16px Arial,sans-serif;color:var(--purple-text)}
.body-copy{position:absolute;top:487px;left:88px;width:625px;text-align:center;font:400 9.5px/15.5px Arial,sans-serif;color:#555}
.pill-btn{position:absolute;height:18px;background:var(--teal);color:#fff;font:700 9px/18px "Open Sans",sans-serif;padding-left:5px}

/* how it works */
.how{position:absolute;left:0;top:572px;width:801px;height:203px;background:var(--grey-bg)}
.section-title{position:absolute;width:801px;text-align:center;font:600 16px/1 "Open Sans",sans-serif;color:#555}
.step{position:absolute;top:76px;width:120px;text-align:center}
.step-badge{width:66px;height:66px;margin:0 auto;border-radius:50%;background:#fff;border:3px solid var(--cyan);display:flex;align-items:center;justify-content:center}
.step-label{margin-top:17px;font:400 11px/1 "Open Sans",sans-serif;color:#444;letter-spacing:.3px}

/* blue band */
.band{position:absolute;left:0;top:775px;width:801px;height:243px;background:var(--cyan)}
.band-title{position:absolute;top:25px;font:600 15px/1 "Open Sans",sans-serif;color:#fff}
.band-rule{position:absolute;top:51px;height:1px;border-top:1px dotted rgba(255,255,255,.6)}
.pager{position:absolute;top:28px;display:flex;gap:3px}
.pager i{width:12px;height:12px;border:1px solid #fff;border-radius:50%}
.quote{position:absolute;left:88px;top:63px;width:294px;height:124px;background:#fff;border-radius:3px;padding:9px 9px;font:italic 400 8px/16px "Open Sans",sans-serif;color:#444}
.quote strong{font-weight:700}
.avatar{position:absolute;left:104px;top:948px;width:54px;height:54px;border-radius:50%;background:radial-gradient(circle at 50% 40%,#8a9bb0,#3d4a5c);border:3px solid #fff}
.client-name{position:absolute;left:172px;top:980px;font:400 11px/1 "Lato",sans-serif;color:#fff}
.news{position:absolute;left:419px;width:295px}
.date{position:absolute;left:0;top:0;width:33px;height:37px;background:#555;color:#fff;text-align:center}
.date b{display:block;font:700 13px/19px "Open Sans",sans-serif}
.date span{display:block;background:#333;font:600 9px/18px "Open Sans",sans-serif}
.news h3{margin-left:46px;font:400 11.5px/1 "Lato",sans-serif;color:#fff;margin-top:-1px}
.news p{margin-left:46px;margin-top:6px;font:400 8.5px/13.5px "Open Sans",sans-serif;color:#fff}

/* footer */
.site-footer{position:absolute;left:0;top:1018px;width:801px;height:160px;background:var(--footer);color:#fff}
.col-title{position:absolute;top:24px;font:400 10px/1 "Open Sans",sans-serif;color:#fff}
.col-title::after{content:"";display:inline-block;width:22px;height:1px;background:#555;vertical-align:middle;margin-left:6px}
.links{position:absolute;left:88px;top:47px;font:400 8.5px/20.5px "Open Sans",sans-serif}
.contact-row{position:absolute;left:230px;display:flex;gap:9px;font:400 8px/12px "Open Sans",sans-serif}
.contact-row svg{flex:none}
.field{position:absolute;left:409px;width:143px;height:17px;background:#fff;color:#888;font:400 8px/17px "Open Sans",sans-serif;padding-left:4px}
.subscribe{position:absolute;left:409px;top:122px;width:59px;height:17px;background:#666;border-radius:2px;font:600 8.5px/17px "Open Sans",sans-serif;text-align:center}
.social{position:absolute;left:600px;display:flex;align-items:center;gap:5px}
.social i{width:24px;height:24px;border-radius:50%}
.social b{display:block;font:400 10px/1 "Open Sans",sans-serif}
.social small{display:block;font:400 7px/1 "Open Sans",sans-serif;color:#999;margin-top:2px;letter-spacing:.4px}
.copyright{position:absolute;left:0;top:1178px;width:801px;height:22px;background:var(--footer-bar);color:#ddd;text-align:center;font:400 8px/22px "Open Sans",sans-serif}
</style>
</head>
<body>

<header class="site-header">
  <svg class="header-band" width="801" height="63" viewBox="0 0 801 63">
    <defs><linearGradient id="band" x1="0" x2="0" y1="0" y2="1"><stop offset="0" stop-color="#8a79cf"/><stop offset="1" stop-color="#6f5fbc"/></linearGradient></defs>
    <polygon points="289,0 801,0 801,63 315,63 300,32" fill="url(#band)"/>
    <polygon points="282,0 289,0 300,32 315,63 308,63 293,32" fill="#fff"/>
  </svg>
  <div class="brand"><span class="brand-dot"></span><span class="brand-name">Brivelle</span></div>
  <div class="brand-tag">HEALTH CARE AND HUMAN SERVICE TECHNOLOGY SOLUTIONS</div>
  <div class="top-actions">
    <span class="top-btn"><svg viewBox="0 0 10 10"><rect x="3" y="1" width="4" height="8" rx="1" fill="none" stroke="#fff"/></svg>1-555-014-7081</span>
    <span class="top-btn"><svg viewBox="0 0 10 10"><circle cx="5" cy="3.2" r="2.2" fill="#fff"/><path d="M1 10 Q5 4 9 10Z" fill="#fff"/></svg>About Us</span>
    <span class="top-btn"><svg viewBox="0 0 10 10"><circle cx="5" cy="5" r="4.2" fill="none" stroke="#fff"/><path d="M5 2.5v4M3.3 5l1.7 1.8L6.7 5" stroke="#fff" fill="none"/></svg>Demo</span>
  </div>
  <nav class="main-nav"><span>Home</span><span>How It Works</span><span>Services</span><span>Training and Transition</span><span>Contact US</span></nav>
</header>

<section class="hero" role="img" aria-label="Black and white photo of a businessman touching a glowing world map network"></section>
<div class="hero-card">
  <div class="h-cond">WE ARE A</div>
  <div class="h-sans">Web-based Healthcare</div>
  <div class="h-cond lg">MANAGEMENT SYSTEM</div>
  <span class="hero-more">Read More<i></i></span>
</div>

<section class="welcome">
  <div class="welcome-title">Welcome to <span class="mark"><b></b>Brivelle</span></div>
  <div class="rule" style="left:300px;top:426px;width:230px"></div>
  <p class="lead">Ut wisi enim ad minim veniam, quis nostrud exerci tation ullamcorper suscipit lobortis nisl ut aliquip ex ea commodo dignissim qui blandit adipiscing consequat.</p>
  <p class="body-copy">Duis autem vel eum iriure dolor in hendrerit in vulputate velit esse molestie consequat, vel illum dolore eu feugiat nulla facilisis at vero eros et accumsan et iusto odio dignissim qui blandit praesent luptatum zzril delenit augue duis dolore te feugait nulla facilisi.</p>
  <span class="pill-btn" style="left:361px;top:534px;width:79px">Read more
    <svg class="abs" style="right:3px;top:3px" width="12" height="12" viewBox="0 0 12 12"><circle cx="6" cy="6" r="5.2" fill="none" stroke="#fff"/><path d="M5 3.5L7.5 6 5 8.5" stroke="#fff" fill="none"/></svg>
  </span>
</section>

<section class="how">
  <h2 class="section-title" style="top:21px">HOW IT WORKS</h2>
  <div class="rule" style="left:320px;top:47px;width:160px"></div>

  <div class="step" style="left:107px">
    <div class="step-badge"><svg width="30" height="30" viewBox="0 0 30 30"><circle cx="12" cy="12" r="8" fill="none" stroke="#444" stroke-width="2.5"/><path d="M18 18l8 8" stroke="#444" stroke-width="3.5" stroke-linecap="round"/></svg></div>
    <div class="step-label">TRACKING</div>
  </div>
  <div class="step" style="left:263px">
    <div class="step-badge"><svg width="30" height="30" viewBox="0 0 30 30"><rect x="3" y="6" width="22" height="19" rx="2" fill="none" stroke="#444" stroke-width="2"/><path d="M3 11h22M8 3v6M20 3v6" stroke="#444" stroke-width="2"/><circle cx="22" cy="23" r="5" fill="#fff" stroke="#444" stroke-width="2"/><path d="M22 21v2.5h2" stroke="#444" stroke-width="1.5" fill="none"/></svg></div>
    <div class="step-label">SCHEDULING</div>
  </div>
  <div class="step" style="left:420px">
    <div class="step-badge"><svg width="32" height="30" viewBox="0 0 32 30"><rect x="8" y="4" width="20" height="12" rx="1.5" fill="none" stroke="#444" stroke-width="2"/><path d="M8 8h20" stroke="#444" stroke-width="2"/><path d="M2 20h8l6 3h9l3-3" stroke="#444" stroke-width="2.5" fill="none" stroke-linejoin="round"/></svg></div>
    <div class="step-label">PAYROLL</div>
  </div>
  <div class="step" style="left:576px">
    <div class="step-badge"><svg width="26" height="30" viewBox="0 0 26 30"><rect x="4" y="3" width="18" height="24" rx="2" fill="none" stroke="#444" stroke-width="2.2"/><path d="M8 10h10M8 15h10M8 20h7" stroke="#444" stroke-width="2"/></svg></div>
    <div class="step-label">BILLING</div>
  </div>

  <svg class="abs" style="left:226px;top:110px" width="48" height="20" viewBox="0 0 48 20"><path d="M2 12 Q22 20 44 8" fill="none" stroke="var(--cyan)" stroke-width="3"/><path d="M36 5l9 3-6 7" fill="none" stroke="var(--cyan)" stroke-width="3"/></svg>
  <svg class="abs" style="left:382px;top:110px" width="48" height="20" viewBox="0 0 48 20"><path d="M2 12 Q22 20 44 8" fill="none" stroke="#7fdbe0" stroke-width="3"/><path d="M36 5l9 3-6 7" fill="none" stroke="#7fdbe0" stroke-width="3"/></svg>
  <svg class="abs" style="left:540px;top:110px" width="48" height="20" viewBox="0 0 48 20"><path d="M2 12 Q22 20 44 8" fill="none" stroke="var(--purple)" stroke-width="3"/><path d="M36 5l9 3-6 7" fill="none" stroke="var(--purple)" stroke-width="3"/></svg>
</section>

<section class="band">
  <h2 class="band-title" style="left:88px">CLIENT TESTIMONIALS</h2>
  <div class="pager" style="left:352px"><i></i><i></i></div>
  <div class="band-rule" style="left:88px;width:294px"></div>
  <div class="quote"><strong>“ Lorem ipsum dolor sit amet, consectetuer adipiscing elit</strong><br>Sed diam nonummy nibh euismod tiidunt ut laoreet dolor magna aliqm erat volutpat Ut wisi enim ad minim veniam, quis nostrudxeon ullcoper suscipit lobortis nis volpat.Ut wisi enim ad minim veniam, quis nostrud exerci tation ullcoper suscipit lobortis nis volpat.Ut wisi enim ad minim iam, quis nostrud exerci tation ullcoper suscipit lobortis nis volpat.</div>
  <svg class="abs" style="left:262px;top:186px" width="50" height="14" viewBox="0 0 50 14"><polygon points="0,0 50,0 4,14" fill="#fff"/></svg>

  <h2 class="band-title" style="left:419px">LATEST NEWS</h2>
  <div class="pager" style="left:684px"><i></i><i></i></div>
  <div class="band-rule" style="left:419px;width:295px"></div>

  <article class="news" style="top:62px">
    <div class="date"><b>01</b><span>OCT</span></div>
    <h3>Lorem ipsum dolor amet consteter adipiing...</h3>
    <p>quis nostrudxeon ullcoper suscipit lobortis nis volpat.Ut wisi enim ad minim veniam, quis nostrud exerci tation per suscipit lobortis nis volpat.Ut wisi e</p>
  </article>
  <div class="band-rule" style="left:419px;width:295px;top:127px"></div>
  <article class="news" style="top:141px">
    <div class="date"><b>01</b><span>OCT</span></div>
    <h3>Lorem ipsum dolor amet consteter adipiing...</h3>
    <p>quis nostrudxeon ullcoper suscipit lobortis nis volpat.Ut wisi enim ad minim veniam, quis nostrud exerci tation per.</p>
  </article>
  <span class="pill-btn" style="left:419px;top:203px;width:62px;font-size:8px;background:#4dd6d6;color:#234">READ MORE »</span>
</section>
<div class="avatar" role="img" aria-label="Portrait photo of the client"></div>
<div class="client-name">— Marlo Venning</div>

<footer class="site-footer">
  <h4 class="col-title" style="left:88px">Quick Link</h4>
  <div class="links">Home<br>About Us<br>Training and Transition<br>How It Works<br>Contact us</div>

  <h4 class="col-title" style="left:231px">CONTACT ADDRESS</h4>
  <div class="contact-row" style="top:45px"><svg width="10" height="14" viewBox="0 0 10 14"><path d="M5 0a5 5 0 0 1 5 5c0 4-5 9-5 9S0 9 0 5a5 5 0 0 1 5-5z" fill="#fff"/><circle cx="5" cy="5" r="1.8" fill="#222"/></svg><span>418 Harlow Ave Suite 2<br>Dunmore City,<br>NJ 07000</span></div>
  <div class="contact-row" style="top:90px;font-size:10px"><svg width="10" height="12" viewBox="0 0 10 12"><rect x="2" y="0.5" width="6" height="11" rx="1" fill="none" stroke="#fff"/></svg><span>1-555-014-7081</span></div>
  <div class="contact-row" style="top:113px"><svg width="12" height="10" viewBox="0 0 12 10"><rect x="0.5" y="1.5" width="11" height="8" fill="none" stroke="#fff"/><path d="M0.5 1.5L6 6l5.5-4.5" fill="none" stroke="#fff"/></svg><span>info@brivellecare.example</span></div>

  <h4 class="col-title" style="left:409px">NEWS LATTER SIGNUP</h4>
  <p class="abs" style="left:410px;top:46px;width:145px;font:400 8px/12px 'Open Sans',sans-serif">Signup with us and get update in your inbox.</p>
  <div class="field" style="top:73px">Your Name</div>
  <div class="field" style="top:97px">Email address</div>
  <div class="subscribe">Subscribe</div>

  <h4 class="col-title" style="left:601px">SOCAIL CONNECT</h4>
  <div class="social" style="top:49px"><i style="background:#3b5998"></i><div><b>FRIENDSPACE</b><small>BECOME A FAN</small></div></div>
  <div class="social" style="top:82px"><i style="background:#d9462f"></i><div><b>CIRCLEPLUS</b><small>ADD TO CIRCLES</small></div></div>
  <div class="social" style="top:115px"><i style="background:#1fb3e6"></i><div><b>CHIRPLINE</b><small>JOIN US</small></div></div>

  <svg class="abs" style="left:0;top:20px" width="801" height="120"><path d="M203 0v120M385 0v120M576 0v120" stroke="#333"/></svg>
</footer>
<div class="copyright">Copyright ©2011 Brivelle Medical LLC. All Rights Reserved.</div>

</body>
</html>
```